Business Card Design Project

I have just chosen a logo and would now like this designed onto a business card for my hair salon. I would like it to be classy not to busy and have a wow factor when people look at them
Has to Include on card:
Logo Design
And business details below
Kellie-ann Drummond (owner)
0482 736 219
Rdw@vomblet.com.au
71 Willowmere Rise Corvin Cove
Logo is now attached please provide designs
Hair

```html
<!DOCTYPE html>
<html lang="en">
<head>
<meta charset="utf-8">
<title>Lumiere Hair Studio – Business Card</title>
<link rel="stylesheet" href="https://fonts.googleapis.com/css2?family=Arimo:wght@400;700&display=swap">
<style>
  :root {
    --backdrop: #8a7a3e;
    --teal: #7fd2de;
    --mist: #f4f7f8;
    --blush: #f5bcd3;
    --rose: #e23478;
    --brand: #c81e6a;
    --edge: #b768a6;
    --photo-deep: #c2125f;
    --photo-mid: #ef5fa0;
    --photo-soft: #b9c9cc;
    --ink-light: #ffffff;
  }
  html, body {
    margin: 0;
    padding: 0;
    width: 1200px;
    height: 928px;
    overflow: hidden;
    background: var(--backdrop);
  }
  .card-stage {
    display: block;
    width: 1200px;
    height: 928px;
  }
  .brand-name {
    font-family: "Arimo", Arial, sans-serif;
    font-weight: 400;
    fill: var(--brand);
    letter-spacing: 3px;
  }
  .salon-address {
    font-family: "Arimo", Arial, sans-serif;
    font-size: 31px;
    fill: var(--brand);
  }
  .contact-line {
    font-family: "Arimo", Arial, sans-serif;
    font-size: 27px;
    fill: var(--ink-light);
  }
</style>
</head>
<body>
<svg class="card-stage" viewBox="0 0 1200 928" xmlns="http://www.w3.org/2000/svg">
  <defs>
    <linearGradient id="card-face" x1="0" y1="0" x2="0" y2="1">
      <stop offset="0" stop-color="var(--teal)"/>
      <stop offset="0.42" stop-color="var(--mist)"/>
      <stop offset="0.68" stop-color="var(--blush)"/>
      <stop offset="1" stop-color="var(--rose)"/>
    </linearGradient>
    <linearGradient id="photo-tones" x1="0" y1="0" x2="1" y2="1">
      <stop offset="0" stop-color="var(--photo-soft)"/>
      <stop offset="0.35" stop-color="var(--photo-mid)"/>
      <stop offset="0.7" stop-color="var(--photo-deep)"/>
      <stop offset="1" stop-color="var(--photo-mid)"/>
    </linearGradient>
    <clipPath id="card-shape">
      <path d="M213 196 L1153 196 L1153 872 L247 872 C120 800 45 680 45 540 C45 390 120 260 213 196 Z"/>
    </clipPath>
    <path id="address-arc" d="M630 552 Q890 452 1146 548"/>
  </defs>

  <g class="business-card">
    <path class="card-face" d="M213 196 L1153 196 L1153 872 L247 872 C120 800 45 680 45 540 C45 390 120 260 213 196 Z" fill="url(#card-face)"/>

    <g clip-path="url(#card-shape)">
      <path class="feature-photo" role="img" aria-label="Close-up beauty photo of a made-up eye framed by a bright pink daisy flower"
            d="M40 190 L655 190 L640 880 L40 880 Z" fill="url(#photo-tones)"/>
    </g>

    <path class="card-edge" d="M213 196 L1153 196 L1153 872 L247 872 C120 800 45 680 45 540 C45 390 120 260 213 196 Z"
          fill="none" stroke="var(--edge)" stroke-width="3"/>

    <g class="brand-block">
      <text class="brand-name" x="898" y="318" text-anchor="middle" font-size="60">LUMIERE</text>
      <text class="brand-name" x="898" y="376" text-anchor="middle" font-size="40">HAIR STUDIO</text>
    </g>

    <text class="salon-address">
      <textPath href="#address-arc" startOffset="50%" text-anchor="middle">71 Willowmere Rise Corvin Cove</textPath>
    </text>

    <g class="contact-block" text-anchor="end">
      <text class="contact-line" x="1124" y="770">Kellie-ann Drummond</text>
      <text class="contact-line" x="1124" y="800">Rdw@vomblet.com.au</text>
      <text class="contact-line" x="1124" y="831">0482 736 219</text>
    </g>
  </g>
</svg>
</body>
</html>
```